A4 double sided brochure for progressive, young lawyers

Hi designers, we would like a double sided A4 flyer advertising:

Designers, Side 1 flyer contents:

Main heading #1 on side 1: Wills

A comprehensive, legal Will gives you peace of mind.

It ensures that your wealth is distributed according to your wishes.

As your life changes, so should your Will. It should reflect evolving circumstances, such as:
- separation or divorce
- assets disposed of or acquired
- the birth or death of beneficiaries
- minor beneficiaries coming of age
- the death or incapacity of an executor

Our lawyers will listen to your wishes and provide tailored advice to suit your needs.

Main heading #2 on side 1 : Testamentary Discretionary Trusts

Did you know that your beneficiaries may have to pay tax on property you leave them in your Will? You can better protect them and minimise potential tax by income streaming with testamentary discretionary trusts.

(Note to Designers: I have attached a word document containing information that I would like to appear under this sentence which includes a few paragraphs and a data table. Please include all information from the word document here in a similar kind or format.)

(Our Call to Action): K.T. Marlow Lawyers has a team of experienced lawyers who can advise you on drafting an effective Will.

Call or email one of our friendly Principals, Rohan Marlow or Priya Marlow for a quick, no-obligation quote.

Designers, side 2 flyer content is as follows:

Main heading side 2: Planning Ahead

Estate Planning is not just about having a Will.

It involves your personal, family and business matters, both now and after you pass away.

While it may be as simple as having a Will, it most cases it also involves having Powers of Attorney, Enduring Guardianships and Advance Health Care planning.

Estate planning is about planning ahead for your current lifestyle needs, you retirement plans, your business arrangements, your tax and superannuation position, future events (like divorce, ill-health and family disputes) and ultimately, ensuring your assets go exactly where you want them to.

Simply put, it gives you peace of mind.

Heading #2 on side 2: What else should I consider now?

[Designers, I am happy for you to put the below 3 points into a picture diagram or some kind of list format - whatever looks less boring!

1. A Power of Attorney - This enables you to appoint a trusted person to act on your behalf if you are unable to, or simply don’t wish to, make decisions about your financial and legal affairs.

[DESIGNERS - please highlight, enlarge or emphasize the words 'power of attorney']

2. A Power of Enduring Guardianship - This enables you to appoint a trusted person to act on your behalf if you are unable (through mental incapacity) to make decisions about your health and welfare issues.

[DESIGNERS - please somehow highlight the words 'power of enduring guardianship']

3. An Advance Health Care Plan - This directs your doctors, medical staff and family how you wish to be treated. Remember, you have the right to accept or refuse medical treatment.

[DESIGNERS - please highlight the words 'Advance Health Care Plan']

(Our Call to Action):

K.T. Marlow Lawyers has a team of experienced lawyers who can advise you on preparing a Will, Powers of Attorney and Powers of Enduring Guardianship, estate planning and administration of a deceased estate.

Industry/Entity Type

Legal

Font styles to use
Sans Serif

Requirements
Must have
• Colours should match our logo. See our website www.ktmarlow.com.au also for colours. Please not too much red blocks areas though.
• Our firm name is: K.T. Marlow Lawyers
• Note to designers - Both sides should have contact details of our 2 offices and other contact information including:
• For more information contact our Principals:
• Rohan Marlow or Priya Marlow
• Office locations:
• WATTLE RIDGE:
• Shop 5, 14-32 Dunmore Crescent,
• Wattle Ridge NSW 2219
• Phone: (02) 9384 2175
• FERNCLIFF:
• 7 Kestrel Lane,
• Ferncliff NSW
• Phone: (02) 9673 4809
• Email: admin@ktmarlow.com.au
• Web: www.ktmarlow.come.au
• Connect with us on Facebook:
• www.facebook.com/ktmarlowlawyers
• Must have 2 pages (back and front of flyer). See project description for details.
• I would like all information contained in the project description and all information contained in my word doc attached to be included in the brochure. Please do not edit the words or the structure of the information.
• The data table (in the word doc attached) must be replicated exactly as it appears including the fine print.
Should not have
• Too many block red areas or too much red.
• I want it to be eye catching but not too bright to read.

```html
<!DOCTYPE html>
<html lang="en">
<head>
<meta charset="utf-8">
<title>K.T. Marlow Lawyers – Wills &amp; Planning Ahead Flyer</title>
<link href="https://fonts.googleapis.com/css2?family=Oswald:wght@600;700&family=Roboto+Condensed:wght@400;700&display=swap" rel="stylesheet">
<style>
:root{
  --red:#a51e22;
  --red-dark:#8f1a1d;
  --yellow:#fde326;
  --amber:#f8b416;
  --ink:#231f20;
  --paper:#ffffff;
  --stage:#3b2a21;
}
*{box-sizing:border-box;margin:0;padding:0}
html,body{width:1200px;height:1200px;overflow:hidden;background:var(--stage)}
body{font-family:"Roboto Condensed","Arial Narrow",Arial,sans-serif;color:var(--ink)}
.stage{position:absolute;left:0;top:0;width:1500px;height:1500px;transform:scale(.8);transform-origin:0 0}
.page{position:absolute;width:687px;height:972px;background:var(--paper);overflow:hidden}
.page--front{left:50px;top:106px}
.page--back{left:765px;top:421px}
.abs{position:absolute}
.photo{position:absolute;background:linear-gradient(135deg,#f3d9c6,#c99a7d 45%,#8fb3d6);border-radius:4px}
.photo--seniors{background:linear-gradient(160deg,#e9c79a,#b98a5a 50%,#6b6f74)}
.display{font-family:"Oswald",Impact,sans-serif;font-weight:700;color:var(--red);line-height:1}
.brand{left:40px;top:36px;color:var(--red);font-weight:700;font-size:34px;line-height:1;text-align:center;width:240px}
.brand span{display:block;font-size:17px;letter-spacing:3px;margin-top:6px}
.lead{font-size:24px;line-height:1.07}
.yellow{background:linear-gradient(90deg,var(--yellow),var(--amber))}
.changes{left:0;top:310px;width:345px;height:292px;padding:10px 10px 0 32px}
.changes h3{font-size:17.5px;font-weight:700;line-height:1.38}
.changes p.cta{font-size:17.5px;font-weight:700;line-height:1.27}
.changes ul{list-style:none;margin:4px 0 3px}
.changes li{font-size:15.5px;line-height:29.5px;padding-left:21px;position:relative}
.changes li::before{content:"";position:absolute;left:2px;top:11px;width:9px;height:9px;border-radius:50%;background:var(--ink)}
.body-sm{font-size:12.4px;line-height:1.35;text-align:justify}
.subhead{font-size:16px;font-weight:700;color:var(--red)}
.tiny{font-size:9.6px;line-height:1.45}
.flow-box{position:absolute;top:730px;height:76px;background:#fff;border-radius:5px;font-size:11px;line-height:1.3;text-align:center;padding:4px 3px}
.saved{left:155px;top:818px;font-size:15px;font-weight:700;color:var(--red)}
.rates{position:absolute;left:433px;top:714px;width:224px;border-collapse:collapse;font-size:11px}
.rates th,.rates td{border:1px solid #555;text-align:center;height:16.5px;padding:0 2px}
.rates th{font-weight:700;height:24px;font-size:11px}
.rates th.tt{font-size:9px;line-height:1}
.rates td.hl{background:var(--red);color:#fff}
.footer{position:absolute;left:0;bottom:0;width:687px;height:95px;background:var(--red);color:#fff;display:flex;align-items:center;text-align:center;font-size:11.5px;line-height:1.3}
.footer .col{padding:0 8px}
.footer .col+.col{border-left:1px solid rgba(255,255,255,.8)}
.footer b{font-weight:700}
.footer .principals{width:160px;font-size:11px}
.footer .principals b.name{font-size:13px;line-height:1.35}
.footer .office1{width:183px}
.footer .office2{width:114px}
.footer .web{flex:1;font-size:12px}
.consider{left:0;top:460px;width:687px;height:325px}
.item h4{font-size:17px;font-weight:700;margin-bottom:14px}
.item p{font-size:13.5px;line-height:1.26}
</style>
</head>
<body>
<main class="stage">

  <section class="page page--front">
    <div class="abs brand">K.T. MARLOW<span>LAWYERS</span></div>
    <div class="photo" style="left:305px;top:20px;width:362px;height:176px" role="img" aria-label="Photograph of a smiling young family of four lying together"></div>

    <h1 class="abs display" style="left:31px;top:135px;font-size:66px">Wills</h1>
    <p class="abs lead" style="left:32px;top:206px">A comprehensive, legal Will gives you peace of mind.</p>
    <p class="abs lead" style="left:32px;top:242px">It ensures that your wealth is distributed<br>according to your wishes.</p>

    <div class="abs yellow changes">
      <h3>As your life changes, so should your Will. It should reflect evolving circumstances, such as</h3>
      <ul>
        <li>Separation or divorce</li>
        <li>Assets disposed of or acquired</li>
        <li>The birth or death of beneficiaries</li>
        <li>Minor beneficiaries coming of age</li>
        <li>The death or incapacity of an executor</li>
      </ul>
      <p class="cta">Our lawyers will listen to your wishes and provide tailored advice to suit your needs.</p>
    </div>

    <h2 class="abs display" style="left:368px;top:340px;font-size:46px;line-height:1.02;letter-spacing:.3px">TESTAMENTARY<br>DISCRETIONARY<br>TRUSTS</h2>
    <p class="abs body-sm" style="left:368px;top:494px;width:290px">Did you know that your beneficiaries may have to pay tax on property you leave them in your Will? You can better protect them and minimise potential tax by income streaming with testamentary discretionary trusts.</p>

    <h3 class="abs subhead" style="left:0;width:687px;top:612px;text-align:center">Income streaming with testamentary discretionary trusts</h3>
    <p class="abs tiny" style="left:32px;top:636px;width:628px;font-size:9.8px;line-height:1.42">When a beneficiary in your Will earns income from a gift-eg. rent on an investment property, or capital gains when they sell it - that income will be taxable. While they have children under 18 years old, that income can be ‘streamed’ to the kids to take advantage of their preferential tax rates. This requires a special structure called a ‘testamentary discretionary trust’ that can only be created under a Will.</p>

    <h3 class="abs subhead" style="left:32px;top:689px;font-size:15px">Mary earns $180K salary and has 4 kids under 18 years old</h3>
    <h3 class="abs subhead" style="left:433px;top:689px;font-size:15px">Income tax rates for resident minors</h3>

    <svg class="abs" style="left:0;top:700px" width="430" height="170" viewBox="0 0 430 170" aria-hidden="true">
      <defs>
        <linearGradient id="flowGold" x1="0" x2="1">
          <stop offset="0" stop-color="#f3c21a"/><stop offset="1" stop-color="#fde34a"/>
        </linearGradient>
      </defs>
      <path d="M33 104 L33 162 L150 112 Z" fill="#d9a514"/>
      <path d="M33 27 Q33 20 40 20 L350 20 L350 14 L415 69 L350 124 L350 110 L40 110 Q33 110 33 103 Z" fill="url(#flowGold)"/>
      <path d="M33 162 L150 112 L150 128 Z" fill="#c08f10"/>
    </svg>
    <div class="flow-box" style="left:42px;width:83px">Jane leaves an investment property worth $1M to her daughter Mary</div>
    <div class="flow-box" style="left:131px;width:89px">Five years later, Mary sells the property for $1.3M, making a $300K capital gain</div>
    <div class="flow-box" style="left:226px;width:145px">Using a ‘simple’ Will :<br>Tax = 47% x $300K = $141K<br>Using a Testamentary Trust :<br>($75K streamed to each child)<br>Tax =$15,922 x 4 = $63,688</div>
    <p class="abs saved">TAX SAVED: $77,312</p>

    <table class="rates">
      <tr><th>Distribution ($)</th><th>Family Trust</th><th class="tt">Testamentary<br>Trust</th></tr>
      <tr><td>0 – 416</td><td></td><td></td></tr>
      <tr><td>417 – 1,307</td><td>66%*</td><td></td></tr>
      <tr><td>1,308 – 18,200</td><td>47%*</td><td></td></tr>
      <tr><td>1,308 – 18,200</td><td>47%*</td><td class="hl">19%</td></tr>
      <tr><td>37,001 – 80,000</td><td>47%*</td><td class="hl">32.5%</td></tr>
      <tr><td>80,001 – 180,000</td><td>47%*</td><td class="hl">37%</td></tr>
    </table>

    <p class="abs tiny" style="left:0;width:687px;top:848px;text-align:center;font-size:8.6px;line-height:1.35">This document contains only a summary of a discrete part of law and is correct at the date of publication. It is<br>not legal advice. You should always seek legal advice about your individual situation.</p>

    <footer class="footer">
      <div class="col principals"><b>For more information<br>contact our Principals</b><br><b class="name">Rohan Marlow<br>Priya Marlow</b></div>
      <div class="col office1"><b>WATTLE RIDGE</b><br>Shop 5, 14-32 Dunmore Crescent,<br>Wattle Ridge NSW 2219<br><b>(02) 9384 2175</b></div>
      <div class="col office2"><b>FERNCLIFF</b><br>7 Kestrel Lane,<br>Ferncliff NSW<br><b>(02) 9673 4809</b></div>
      <div class="col web">admin@ktmarlow.com.au<br>www.ktmarlow.come.au<br>www.facebook.com /ktmarlowlawyers</div>
    </footer>
  </section>

  <section class="page page--back">
    <h1 class="abs display" style="left:30px;top:24px;font-size:64px">Planning Ahead</h1>
    <p class="abs lead" style="left:31px;top:101px">Estate Planning is not just about having a Will.</p>
    <p class="abs lead" style="left:31px;top:140px">It involves your personal, family and business matters,<br>both now and after you pass away.</p>
    <p class="abs body-sm" style="left:33px;top:214px;width:623px">While it may be as simple as having a Will, it most cases it also involves having Powers of Attorney, Enduring Guardianships and Advance Health Care planning.</p>
    <p class="abs body-sm" style="left:33px;top:263px;width:623px">Estate planning is about planning ahead for your current lifestyle needs, you retirement plans, your business arrangements, your tax and superannuation position, future events (like divorce, ill-health and family disputes) and ultimately, ensuring your assets go exactly where you want them to.</p>
    <h3 class="abs" style="left:32px;top:322px;font-size:27px;font-weight:700">Simply put, it gives you peace of mind</h3>
    <h2 class="abs display" style="left:32px;top:364px;font-size:46px;line-height:1.02;letter-spacing:.3px">WHAT ELSE<br>SHOULD I CONSIDER NOW?</h2>

    <div class="abs yellow consider">
      <div class="photo photo--seniors" style="left:0;top:0;width:335px;height:325px;border-radius:0" role="img" aria-label="Photograph of three generations of a family gathered around grandparents on a wooden bench"></div>
      <div class="abs item" style="left:352px;top:16px;width:305px">
        <h4>A Power of Attorney</h4>
        <p>&nbsp;This enables you to appoint a trusted person to act on your behalf if you are unable to, or simply don’t wish to, make decisions about your financial and legal affairs.</p>
      </div>
      <div class="abs item" style="left:352px;top:118px;width:305px">
        <h4>A Power of Enduring Guardianship</h4>
        <p>This enables you to appoint a trusted person to act on your behalf if you are unable (through mental incapacity) to make decisions about your health and welfare issues.</p>
      </div>
      <div class="abs item" style="left:352px;top:218px;width:305px">
        <h4>An Advance Health Care Plan</h4>
        <p>This directs your doctors, medical staff and family how you wish to be treated. Remember, you have the right to accept or refuse medical treatment.</p>
      </div>
    </div>

    <p class="abs" style="left:33px;top:800px;width:630px;font-size:16.5px;line-height:1.28">K.T. Marlow Lawyers has a team of experienced lawyers who can advise you on preparing a Will, Powers of Attorney and Powers of Enduring Guardianship, estate planning and administration of a deceased estate.</p>

    <footer class="footer" style="height:93px">
      <div class="col principals"><b>For more information<br>contact our Principals</b><br><b class="name">Rohan Marlow<br>Priya Marlow</b></div>
      <div class="col office1"><b>WATTLE RIDGE</b><br>Shop 5, 14-32 Dunmore Crescent,<br>Wattle Ridge NSW 2219<br><b>(02) 9384 2175</b></div>
      <div class="col office2"><b>FERNCLIFF</b><br>7 Kestrel Lane,<br>Ferncliff NSW<br><b>(02) 9673 4809</b></div>
      <div class="col web">admin@ktmarlow.com.au<br>www.ktmarlow.come.au<br>www.facebook.com /ktmarlowlawyers</div>
    </footer>
  </section>

</main>
</body>
</html>
```